plumbers buisness card

A buisness card for a plumbing buisness
needs to have a water theme with navy blue, light blue and white
with an image of either a water drop, pipes, tools or something relating to plumbing and incorperating my buisness name as a logo

"Talcott Plumbing" is the words that need to stand out with "& gasfitting" to be smaller
Updates

spelling error on brief, "maintenance"
and also could you include my email m_talcott@nimbrel.com.au

Industry/Entity Type

Plumbing

Contact Information for Business Card

Talcott Plumbing & Gasfitting

myles talcott
0492315806

specialising in
-new homes
-maitenance
-renovations

license no.
-73846

```html
<!DOCTYPE html>
<html lang="en">
<head>
<meta charset="utf-8">
<title>Talcott Plumbing &amp; Gasfitting – Business Card</title>
<link rel="stylesheet" href="https://fonts.googleapis.com/css2?family=Questrial&family=Arimo:wght@400;700&family=Tinos:ital@1&display=swap">
<style>
  :root {
    --page: #ffffff;
    --navy-deep: #0f1d52;
    --navy: #1a2d80;
    --royal: #1f46ad;
    --sky-light: #dff6fc;
    --sky-mid: #8fdcf4;
    --sky-deep: #4fb2e6;
    --ink: #101010;
    --white: #ffffff;
    --lime: #e4f53f;
    --bullet: #e0283a;
  }
  html, body {
    margin: 0;
    padding: 0;
    width: 724px;
    height: 1200px;
    overflow: hidden;
    background: var(--page);
  }
  .card {
    position: absolute;
    left: 41px;
    top: 36px;
    width: 648px;
    height: 1109px;
    background: var(--navy);
    overflow: hidden;
  }
  .card__body {
    position: absolute;
    left: 37px;
    width: 581px;
    top: 0;
    bottom: 0;
    background:
      linear-gradient(90deg, rgba(31,70,173,0.55) 0%, rgba(31,70,173,0) 14%, rgba(31,70,173,0) 86%, rgba(31,70,173,0.55) 100%),
      linear-gradient(180deg, var(--sky-mid) 0%, var(--sky-light) 45%, var(--sky-mid) 70%, var(--sky-deep) 100%);
  }
  .name-band {
    position: absolute;
    left: 37px;
    width: 581px;
    top: 32px;
    height: 56px;
    background: var(--royal);
    color: var(--white);
    font-family: "Questrial", sans-serif;
    font-size: 39px;
    line-height: 56px;
    text-align: center;
  }
  .logo-box {
    position: absolute;
    left: 85px;
    top: 199px;
    width: 478px;
    height: 362px;
    background: var(--white);
    border: 2px solid var(--navy-deep);
    box-sizing: border-box;
    display: flex;
    flex-direction: column;
    justify-content: center;
    align-items: center;
    font-family: "Questrial", sans-serif;
    color: var(--royal);
    text-align: center;
    line-height: 1.1;
  }
  .logo-box__name { font-size: 66px; }
  .logo-box__trade { font-size: 52px; }
  .logo-box__sub { font-size: 38px; margin-top: 10px; }
  .phone {
    position: absolute;
    left: 291px;
    top: 748px;
    height: 36px;
    font-family: "Arimo", sans-serif;
    font-size: 30px;
    line-height: 36px;
    color: var(--ink);
    white-space: nowrap;
  }
  .label { font-weight: 700; }
  .contact-panel {
    position: absolute;
    left: 120px;
    top: 784px;
    width: 425px;
    height: 303px;
    background: var(--royal);
  }
  .email {
    position: absolute;
    left: 120px;
    top: 784px;
    width: 425px;
    height: 46px;
    padding-left: 10px;
    box-sizing: border-box;
    font-family: "Arimo", sans-serif;
    font-size: 28px;
    line-height: 46px;
    color: var(--white);
    white-space: nowrap;
  }
  .services {
    position: absolute;
    left: 59px;
    top: 852px;
    width: 456px;
    height: 181px;
    background: var(--navy-deep);
  }
  .services__art {
    position: absolute;
    left: 0;
    top: 0;
    width: 170px;
    height: 181px;
  }
  .services__title {
    position: absolute;
    left: 234px;
    top: 0;
    font-family: "Tinos", serif;
    font-style: italic;
    font-size: 31px;
    line-height: 32px;
    color: var(--white);
    white-space: nowrap;
  }
  .services__list {
    position: absolute;
    left: 205px;
    top: 34px;
    margin: 0;
    padding: 0;
    list-style: none;
    font-family: "Arimo", sans-serif;
    font-size: 30px;
    line-height: 44px;
    color: var(--lime);
  }
  .services__list li {
    display: flex;
    align-items: center;
    height: 44px;
    white-space: nowrap;
  }
  .services__list li::before {
    content: "";
    width: 11px;
    height: 11px;
    border: 2px solid var(--bullet);
    border-radius: 50%;
    margin-right: 14px;
  }
  .licence {
    position: absolute;
    left: 291px;
    top: 1047px;
    font-family: "Arimo", sans-serif;
    font-size: 23px;
    line-height: 28px;
    color: var(--white);
    white-space: nowrap;
  }
</style>
</head>
<body>
  <div class="card">
    <div class="card__body"></div>

    <div class="name-band">Myles Talcott</div>

    <div class="logo-box">
      <div class="logo-box__name">Talcott</div>
      <div class="logo-box__trade">Plumbing</div>
      <div class="logo-box__sub">&amp; Gasfitting</div>
    </div>

    <div class="phone"><span class="label">T:</span> 0492315806</div>
    <div class="contact-panel"></div>
    <div class="email"><span class="label">E:</span> m_talcott@nimbrel.com.au</div>

    <div class="services">
      <svg class="services__art" viewBox="0 0 170 181" role="img" aria-label="Illustration of a tap with a falling water drop">
        <defs>
          <linearGradient id="tapTone" x1="0" y1="0" x2="1" y2="1">
            <stop offset="0" stop-color="#4d7fa8"/>
            <stop offset="1" stop-color="#1a3a6a"/>
          </linearGradient>
        </defs>
        <rect width="170" height="181" fill="url(#tapTone)" opacity="0.55"/>
      </svg>
      <div class="services__title">Specialising in</div>
      <ul class="services__list">
        <li>New Homes</li>
        <li>Maintenance</li>
        <li>Renovations</li>
      </ul>
    </div>

    <div class="licence">license no.73846</div>
  </div>
</body>
</html>
```